Electrician Letterhead Design BLR

We need some letterhead for our bills and other papers.
Customer address is on the right side (Swiss format)
A4 format

Design should also be applicable on Cards

Target Market(s)

Private Customers, Small Business

Industry/Entity Type

Electrician

Other font styles liked:
• incised 901

Colors
00AB8E
00BBA5
67D7C9
C6EFE9
E9F9F6

```html
<!DOCTYPE html>
<html lang="en">
<head>
<meta charset="utf-8">
<title>BLR Letterhead</title>
<link rel="stylesheet" href="https://fonts.googleapis.com/css2?family=Arimo:wght@400;700&family=Mulish:wght@600;700&display=swap">
<style>
  :root {
    --brand-teal: #009e8c;
    --ink: #555555;
    --rule-dark: #111111;
    --backdrop: #e4e4e4;
    --paper: #ffffff;
    --signature-tone: #5a5a5a;
  }
  * { margin: 0; padding: 0; box-sizing: border-box; }
  html, body { width: 1189px; height: 1200px; overflow: hidden; }
  body { background: var(--backdrop); font-family: "Arimo", Arial, sans-serif; color: var(--ink); }

  .sheet {
    position: absolute; left: 170px; top: 0;
    width: 849px; height: 1200px;
    background: var(--paper);
  }

  .brand-name {
    position: absolute; left: 76px; top: 40px;
    font-family: "Arimo", Arial, sans-serif; font-weight: 700;
    font-size: 86px; line-height: 1; letter-spacing: 2px;
    color: var(--brand-teal);
  }

  .header-band {
    position: absolute; left: 0; top: 129px; width: 849px; height: 8px;
    background: var(--brand-teal);
  }
  .header-rule {
    position: absolute; left: 0; top: 142px; width: 849px; height: 2px;
    background: var(--rule-dark);
  }
  .company-line {
    position: absolute; left: 70px; top: 126px;
    padding: 0 6px; background: var(--paper);
    font-family: "Arimo", Arial, sans-serif; font-weight: 700;
    font-size: 11px; line-height: 14px; letter-spacing: 0.3px; color: var(--rule-dark);
  }

  .sender-address {
    position: absolute; right: 229px; top: 64px;
    text-align: right; font-size: 13px; line-height: 17px;
  }
  .contact-divider {
    position: absolute; left: 633px; top: 67px; width: 1px; height: 50px;
    background: var(--ink);
  }
  .contact-list {
    position: absolute; left: 646px; top: 64px; list-style: none;
    font-size: 13px; line-height: 17px;
  }
  .contact-list li { display: flex; align-items: center; gap: 7px; }
  .contact-list svg { width: 11px; height: 11px; flex: none; }

  .letter {
    position: absolute; left: 76px; top: 368px; width: 696px;
  }
  .salutation {
    font-family: "Mulish", "Century Gothic", sans-serif; font-weight: 700;
    font-size: 19.5px; color: var(--ink); margin-bottom: 30px;
  }
  .letter p {
    font-size: 13.9px; line-height: 17.5px; margin-bottom: 15px;
  }
  .closing {
    font-family: "Mulish", "Century Gothic", sans-serif; font-weight: 700;
    font-size: 10.6px; margin-top: 23px;
  }
  .signature {
    display: block; margin-top: 32px; width: 140px; height: 36px;
    background: var(--signature-tone); opacity: 0.18; border-radius: 4px;
  }
</style>
</head>
<body>
  <main class="sheet">
    <header>
      <div class="brand-name">BLR</div>
      <div class="header-band"></div>
      <div class="header-rule"></div>
      <div class="company-line">Elektrotechnik Berler GmbH</div>

      <address class="sender-address" style="font-style:normal">
        Your address<br>city<br>state, ZIP 0000
      </address>
      <div class="contact-divider"></div>
      <ul class="contact-list">
        <li>
          <svg viewBox="0 0 12 12" aria-hidden="true"><path fill="var(--brand-teal)" d="M2.5 1l2 2-1 1.3a7 7 0 0 0 4.2 4.2L9 7.5l2 2-1.3 1.5C5 11 1 7 1 2.3z"/></svg>
          123-456-2100
        </li>
        <li>
          <svg viewBox="0 0 12 12" aria-hidden="true"><rect x="1" y="3" width="10" height="7" fill="var(--brand-teal)"/><path d="M1 3l5 4 5-4" stroke="#fff" stroke-width="1" fill="none"/></svg>
          youremail@mailbox.com
        </li>
        <li>
          <svg viewBox="0 0 12 12" aria-hidden="true"><circle cx="6" cy="6" r="5" fill="var(--brand-teal)"/><path d="M1 6h10M6 1c-2 2.5-2 7.5 0 10M6 1c2 2.5 2 7.5 0 10" stroke="#fff" stroke-width="0.8" fill="none"/></svg>
          www.yourwebsite.com
        </li>
      </ul>
    </header>

    <section class="letter">
      <h1 class="salutation">Dear Mr. Smith,</h1>
      <p>Lorem ipsum dolor sit amet, consectetuer adipiscing elit, sed diam nonmmy nibh euismod tincidunt ut laor eet dolore magna aliquam erat volutpat. Ut wisi enim ad minim veniam, quis nostrud exerci tationmcorper suscipit lobortis nisl ut aliquip ex ea commodo consequat. Duis autem vel eum iriure dolor in hendrerit in vulputate velit esse molestie consequat, vel illum dolore eu feugiat</p>
      <p>Rorem ipsum dolor sit amet, consectetuer adipiscing elit, sed diam nonmmy nibh euismod tincidunt ut laor eet dolore magna aliquam erat volutpat. Ut wisi enim ad minim veniam, quis nostrud exerci tationmcorper suscipit lobortis nisl ut aliquip ex ea commodo consequat. Duis autem vel eum iriure dolor in hendrerit in vulputate velit esse molest</p>
      <p>Dorem ipsum dolor sit amet, consectetuer adipiscing elit, sed diam nonmmy nibh euismod tincidunt ut laor eet dolore magna aliquam erat volutpat. Ut wisi enim ad minim veniam, quis nostrud exerci tationmcorper suscipit lobortis nisl ut aliquip ex ea commodo consequat. Duis autem vel eum iriure dolor in hendrerit in suscipit lobortis nisl ut aliquip ex ea commodo consequat. Duis autem vel eum iriure dolor in hendrerit in vulputate velit esse molestie consequat, vel illum</p>
      <p>Sorem ipsum dolor sit amet, consectetuer adipiscing elit, sed diam nonmmy nibh euismod tincidunt ut laor eet dolore magna aliquam erat volutpat. Ut wisi enim ad minim veniam, quis nostrud exerci tationmcorper suscipit lobortis nisl ut aliquip ex ea commodo consequat. Duis autem vel eum iriure dolor in</p>
      <div class="closing">Sincerely,</div>
      <span class="signature" role="img" aria-label="Handwritten signature of the sender"></span>
    </section>
  </main>
</body>
</html>
```